Album art design concept, my band will be releasing a 11 song rock album in the next few Months. We will be using it as a CD cover, poster, online art cover, maybe even Vinyl. Working album titles are "Woven from static" (Preferred album title) or "The river under the stone". Anything abstract, painting-like design, or whatever type of design that comes to mind. Fonts are designers choice. Thank You

Target Market(s)

Music business

Colors

Designer to choose colors to be used in the design.

Requirements
Must have
• Our band logo
Nice to have
• Anything abstract, attractive painting type, maybe even some kind of a futuristic design.
Should not have
• Skulls, blood-like, scary designs, nudity, emo type of design

```html
<!DOCTYPE html>
<html lang="en">
<head>
<meta charset="utf-8">
<title>The River Under the Stone — Lantern Hollow</title>
<link href="https://fonts.googleapis.com/css2?family=Montserrat:wght@600;700&display=swap" rel="stylesheet">
<style>
  :root {
    --backdrop: #1d1d1e;
    --signal-red: #e8454f;
    --snow-white: #f4f5f7;
    --sky-haze: #8d9db2;
    --street-blue: #4f6277;
    --night-teal: #162a33;
    --deep-teal: #11232b;
    --neon-pink: rgba(226, 70, 98, 0.5);
  }
  * { margin: 0; padding: 0; box-sizing: border-box; }
  html, body {
    width: 1200px;
    height: 764px;
    overflow: hidden;
    background: var(--backdrop);
  }
  .stage {
    position: relative;
    width: 1200px;
    height: 764px;
  }
  .album-cover {
    position: absolute;
    left: 352px;
    top: 133px;
    width: 497px;
    height: 497px;
    overflow: hidden;
    font-family: "Montserrat", sans-serif;
  }
  .city-scene {
    position: absolute;
    inset: 0;
    background:
      linear-gradient(90deg, transparent 55%, var(--neon-pink) 72%, transparent 92%),
      linear-gradient(180deg, var(--sky-haze) 0%, var(--street-blue) 32%, var(--night-teal) 58%, var(--deep-teal) 100%);
  }
  .album-title {
    position: absolute;
    right: 309px;
    top: 243px;
    color: var(--signal-red);
    font-weight: 700;
    font-size: 12.5px;
    line-height: 15px;
    letter-spacing: 2.4px;
    text-transform: uppercase;
    text-align: right;
    white-space: nowrap;
  }
  .band-name {
    position: absolute;
    right: 49px;
    top: 427px;
    color: var(--snow-white);
    font-weight: 600;
    font-size: 17px;
    line-height: 18px;
    letter-spacing: 0.5px;
    text-transform: uppercase;
    text-align: right;
    white-space: nowrap;
  }
</style>
</head>
<body>
  <main class="stage">
    <section class="album-cover">
      <div class="city-scene" role="img" aria-label="Photograph of a crowded city square at night in falling snow, people with umbrellas under glowing billboards and red neon signs"></div>

      <h1 class="album-title">The river<br>under the stone</h1>

      <p class="band-name">Lantern<br>Hollow</p>
    </section>
  </main>
</body>
</html>
```